Interior Design/ decoration business card design

This card is for my Interior Design and Decoration business and later I will also be selling homewares. I would like the card to be very simple in design and like either white, duck egg blue , aquas or metallics on a flat mat card excellent quality card. It needs to be well designed as that is my field. I dont like fuss, the simpler the better. I would like a styalised wren under the name wren if possible. SIMPLE, STYLISH, CLASSIC, TASTEFUL

Target Market(s)

40 + year olds who are building or rennovating.

Industry/Entity Type

Business

Contact Information for Business Card

Wren
styling, design, homeware

Marnie Tolland
p 0427316958
e marnie@wrenliving.com.au
w wrenliving.com.au

Requirements
Must have
• very simple, stylish, classic, sophisticated. Simple and easy to read text that is a print similar to attached image. I like simple round A's though not as in attached image.

Double sided. It wont save as double sided for some reason!!
Should not have
• not too much colour, No animated / cartoon pictures.

```html
<!DOCTYPE html>
<html lang="en">
<head>
<meta charset="utf-8">
<title>Wren – Business Card</title>
<link rel="stylesheet" href="https://fonts.googleapis.com/css2?family=Arimo:wght@400;700&family=Sofia&display=swap">
<style>
  :root {
    --backdrop: #cfeeed;
    --card-teal: #7fa39c;
    --ink-teal: #769a94;
    --paper: #ffffff;
    --shadow: rgba(40, 80, 78, 0.22);
  }
  * { box-sizing: border-box; margin: 0; padding: 0; }
  html, body {
    width: 1200px;
    height: 781px;
    overflow: hidden;
  }
  body {
    background: var(--backdrop);
    font-family: "Arimo", Arial, sans-serif;
    position: relative;
  }
  .card {
    position: absolute;
    width: 520px;
    height: 300px;
    box-shadow: 0 6px 18px var(--shadow);
    overflow: hidden;
  }
  .card--front { left: 60px; top: 240px; background: var(--card-teal); }
  .card--back  { left: 620px; top: 240px; background: var(--card-teal); }

  .front-panel { position: absolute; inset: 0; }

  .brand {
    display: flex;
    align-items: center;
    gap: 8px;
    color: var(--paper);
    font-family: "Arimo", Arial, sans-serif;
    font-weight: 700;
  }
  .brand__dot {
    background: var(--paper);
    border-radius: 50%;
    flex: none;
  }

  .front-brand {
    position: absolute;
    left: 28px;
    top: 92px;
    font-size: 24px;
  }
  .front-brand .brand__dot { width: 12px; height: 12px; }

  .tagline-stack {
    position: absolute;
    left: 20px;
    top: 156px;
    width: 130px;
    text-align: center;
    color: var(--paper);
    font-family: "Sofia", cursive;
    font-size: 19px;
    line-height: 1.3;
    list-style: none;
  }
  .tagline-stack .sep { font-family: "Arimo", sans-serif; font-size: 12px; }

  .contact {
    position: absolute;
    right: 30px;
    top: 32px;
    text-align: right;
    color: var(--ink-teal);
  }
  .contact__name {
    font-family: "Sofia", cursive;
    font-size: 38px;
    font-weight: 400;
    margin-bottom: 30px;
  }
  .contact__line {
    font-size: 18px;
    font-weight: 700;
    margin-bottom: 24px;
    font-style: normal;
  }
  .contact__line a { color: inherit; text-decoration: none; }

  .back-brand {
    position: absolute;
    left: 0; right: 0;
    top: 60px;
    justify-content: center;
    font-size: 48px;
    gap: 14px;
  }
  .back-brand .brand__dot { width: 18px; height: 18px; }

  .back-tagline {
    position: absolute;
    left: 0; right: 0;
    bottom: 34px;
    text-align: center;
    color: var(--paper);
    font-family: "Sofia", cursive;
    font-size: 30px;
  }
  .back-tagline .sep { font-family: "Arimo", sans-serif; font-size: 16px; margin: 0 10px; vertical-align: middle; }
</style>
</head>
<body>
  <section class="card card--front" aria-label="Business card front">
    <svg class="front-panel" width="520" height="300" viewBox="0 0 520 300" aria-hidden="true">
      <path d="M200 0 H520 V300 H280 C205 240 160 120 200 0 Z" fill="#ffffff"/>
    </svg>

    <div class="brand front-brand">
      <span>wren</span>
      <span class="brand__dot"></span>
    </div>

    <ul class="tagline-stack">
      <li>styling</li>
      <li class="sep">•</li>
      <li>design</li>
      <li class="sep">•</li>
      <li>homeware</li>
    </ul>

    <div class="contact">
      <h1 class="contact__name">Marnie Tolland</h1>
      <address class="contact__line">042 731 6958</address>
      <address class="contact__line"><a href="mailto:marnie@wrenliving.com.au">marnie@wrenliving.com.au</a></address>
      <address class="contact__line">www.wrenliving.com.au</address>
    </div>
  </section>

  <section class="card card--back" aria-label="Business card back">
    <div class="brand back-brand">
      <span>wren</span>
      <span class="brand__dot"></span>
    </div>
    <p class="back-tagline">styling<span class="sep">•</span>design<span class="sep">•</span>homeware</p>
  </section>
</body>
</html>
```